New Discover Site!!

Hello everyone!
We're WanderlyTrips. A tour company which offer group excursions to places like Morocco & Portugal for young adults. We have been in the business for 10 years now and we'd like to create a new fresh look and feel design. Something clean and more modern.
We offer trips to:
1 - Weekend trips Lagos, Portugal
2 - Weekend tips to Morocco
3 - 5 day trip to the Sahara Desert in Morocco
4 - Beach day trips to Cadiz
5 - Day trip to Gibraltar
6 - Costume trips
7 - Wine Tasting day trip
8 - Fiestas de Marvela
Those are the 8 boxes we'd like to have on our home-page along with an awesome header and footer. You can take a look for our current page to see sections and the text of the sections. Once we approve a nice home page from any of you designers, we will go ahead and send you the names of all the pages we'd like you to design for us. We already have someone who will code all the pages. We just need a new design for all the pages.
You can see our logo on our Blog: http://wanderlytripsblog.example/
We like websites like:
www.Holvaro.com
www.Skarnel.com
We look forward to hear from you!!
PS:
we will need the home page and other pages.
7 pages plus 8 trip pages. The trip pages they can all look the same (design wise) obviusly diferent photos, video and content. Total 15 pages.
Page 1 - Home page
Page 2 - About us. This page can look similar to:
Page 3 - FAQs. This page can look similar to:
Page 4 - Contact us. This page can look similar to: http://www.holvaro.com/contact
Page 5 - Trip check in. This page can look similar to the Skarnel.com look for flight check in. Something clean.
Page 6 - Trip videos. This page, will have the list of all our trip videos. A line or two of the trip and the video right below.
Page 7 - Trip departure info. On this page we're going to have the information on how to get to Sevilla. Also the google map of the actual meeting point and maybe a youtube video somewhere.
Page 8 - Why travel with us.
How many trip page are we going to need?
We have 8 trips. If you can just do 1 page, then you can do the same type page for all the trips. On each trip page you must add the following content:
Trip overview
Whats included
Trip dates
Photos and a youtube video.
An example of our current lagos trip page is:
https://www.wanderlytrips.example/2001/09/beach-getaway-lagos-portugal/
You can take all the content from www.WanderlyTrips.example

```html
<!DOCTYPE html>
<html lang="en">
<head>
<meta charset="utf-8">
<title>WanderlyTrips – Home</title>
<link rel="stylesheet" href="https://fonts.googleapis.com/css2?family=Roboto:wght@400;500;700&family=Ubuntu:wght@400;500;700&display=swap">
<style>
:root{
  --header-top:#3a4452;
  --header-bottom:#283039;
  --stripe:#7d8591;
  --sea-dark:#1d4f86;
  --sea-mid:#3b7ec4;
  --sky:#9cc6ea;
  --panel:rgba(24,30,38,.88);
  --blue:#4a8cf0;
  --blue-dark:#2f6fd6;
  --link:#1a66e8;
  --page:#f7f8fa;
  --ink:#111;
  --footer:#1d1d1d;
  --footer-text:#e4e4e4;
  --white:#fff;
}
*{box-sizing:border-box;margin:0;padding:0}
html,body{width:1200px;height:1179px;overflow:hidden}
body{background:var(--page);font-family:"Ubuntu",sans-serif;color:var(--ink);position:relative}
.wrap{position:absolute;left:171px;width:858px}

/* header */
.site-header{position:absolute;top:0;left:0;width:1200px;height:82px;
  background:linear-gradient(var(--header-top),var(--header-bottom));border-bottom:5px solid var(--stripe)}
.brand{position:absolute;left:171px;top:22px;display:flex;align-items:center;gap:7px;
  font-family:"Roboto",sans-serif;font-weight:700;font-size:17px;color:var(--white)}
.brand-mark{width:14px;height:14px;background:var(--blue)}
.main-nav{position:absolute;left:335px;top:36px;display:flex;gap:25.5px;
  font-family:"Roboto",sans-serif;font-weight:700;font-size:10.5px;color:var(--white);text-transform:uppercase}

/* hero */
.hero{position:absolute;top:82px;left:0;width:1200px;height:347px;
  background:linear-gradient(180deg,var(--sky) 0%,#6ea7dc 25%,var(--sea-mid) 50%,var(--sea-dark) 80%,#2a6aa8 100%);
  border-bottom:5px solid #3b4452}
.hero-title{position:absolute;left:263px;top:34px;width:669px;height:57px;background:var(--panel);
  color:var(--white);font-family:"Roboto",sans-serif;font-weight:700;font-size:26px;
  display:flex;align-items:center;justify-content:center}
.hero-photo{position:absolute;left:171px;top:125px;width:452px;height:150px;
  background:linear-gradient(180deg,#e9e3d8 0%,#dcc9a8 48%,#d49a55 62%,#c98a44 100%)}
.hero-copy{position:absolute;left:649px;top:126px;width:380px;height:149px;background:var(--panel);
  padding:14px 17px;color:var(--white);font-family:"Roboto",sans-serif;font-weight:500;font-size:13px;line-height:21.5px}
.hero-actions{display:flex;align-items:center;gap:14px;margin-top:10px}
.btn{display:inline-flex;align-items:center;justify-content:center;background:linear-gradient(var(--blue),var(--blue-dark));
  color:var(--white);font-family:"Roboto",sans-serif;font-weight:700;border-radius:3px}
.btn-small{width:81px;height:29px;font-size:12px}
.read-more{font-size:11px;font-weight:700}

/* sections */
.section-title{position:absolute;left:0;width:1200px;text-align:center;font-family:"Roboto",sans-serif;font-weight:700;font-size:17px}
.trip-grid{position:absolute;left:171px;top:489px;width:858px;height:86px;background:var(--blue);padding:0 17px}
.trip-row{display:grid;grid-template-columns:repeat(4,1fr);height:42px;align-items:center;text-align:center;
  color:var(--white);font-size:10.5px;font-weight:500;text-shadow:0 1px 1px rgba(0,0,0,.35)}
.trip-row+.trip-row{border-top:1px solid rgba(255,255,255,.25)}

.card{position:absolute;top:643px;width:193px;height:150px;background:var(--white);
  box-shadow:0 0 2px rgba(0,0,0,.25);padding:4px;text-align:center;font-size:10.5px}
.card-photo{height:86px;background:linear-gradient(100deg,#3f8eb2 0%,#6fb1ad 45%,#c29a66 70%,#d7b07a 100%)}
.card-title{font-weight:700;margin-top:8px}
.card-price{margin-top:3px}
.card-link{color:var(--link);font-weight:700;margin-top:3px}
.btn-more{position:absolute;left:484px;top:827px;width:231px;height:39px;font-size:15.5px;font-weight:500}

/* footer */
.site-footer{position:absolute;top:900px;left:0;width:1200px;height:279px;background:var(--footer);border-top:5px solid #7a7a7a;color:var(--footer-text)}
.footer-col{position:absolute;top:20px;font-size:10.5px;line-height:17px}
.footer-col h3{font-family:"Roboto",sans-serif;font-weight:500;font-size:17px;color:var(--white);margin-bottom:6px;line-height:20px}
.footer-col ul{list-style:none}
.social-bar{position:absolute;left:171px;top:201px;width:858px;height:43px;background:var(--blue);
  display:flex;align-items:center;justify-content:space-between;padding:0 9px 0 13px;
  color:var(--white);font-family:"Roboto",sans-serif;font-weight:500;font-size:15.5px;text-shadow:0 1px 1px rgba(0,0,0,.3)}
.social-icons{display:flex;gap:8px}
.social-icon{width:26px;height:26px;border-radius:3px;background:#3c5a99}
.social-icon.video{background:#c9302c}
</style>
</head>
<body>

<header class="site-header">
  <div class="brand"><span class="brand-mark"></span>WanderlyTrips</div>
  <nav class="main-nav">
    <span>Home</span><span>About us</span><span>FAQ</span><span>Contact us</span>
    <span>Trip check in</span><span>Trip videos</span><span>Trip departure info</span><span>Why travel with us</span>
  </nav>
</header>

<section class="hero" role="img" aria-label="Blurred photo of a rocky coastline and blue sea">
  <h1 class="hero-title">Weekend in North Morocco with WanderlyTrips!</h1>
  <div class="hero-photo" role="img" aria-label="Photo of a group riding camels across desert dunes"></div>
  <div class="hero-copy">
    <p>On just the other side of that small channel of water that separates Europe and Africa, lies a whole new world just waiting for you to come and experience all the wonder that it has to offer.</p>
    <div class="hero-actions"><span class="btn btn-small">Book now!</span><span class="read-more">Read more</span></div>
  </div>
</section>

<h2 class="section-title" style="top:452px">We offer these trips!</h2>
<nav class="trip-grid">
  <div class="trip-row"><span>Weekend trips Lagos, Portugal</span><span>Weekend trips to Morocco</span><span>5 day trip to the Sahara Desert</span><span>Beach day trips to Cadiz</span></div>
  <div class="trip-row"><span>Day trip to Gibraltar</span><span>Costume trips</span><span>Wine Tasting day trip</span><span>Fiestas de Marvela</span></div>
</nav>

<h2 class="section-title" style="top:606px">Upcoming Excursions!</h2>
<article class="card" style="left:171px"><div class="card-photo" role="img" aria-label="Photo of a turquoise cove beside sandstone cliffs"></div><div class="card-title">Beach Getaway to Lagos, Portugal!</div><div class="card-price">Price: 139€</div><div class="card-link">Info &amp; Book Now!</div></article>
<article class="card" style="left:392px"><div class="card-photo" role="img" aria-label="Photo of a turquoise cove beside sandstone cliffs"></div><div class="card-title">Beach Getaway to Lagos, Portugal!</div><div class="card-price">Price: 139€</div><div class="card-link">Info &amp; Book Now!</div></article>
<article class="card" style="left:614px"><div class="card-photo" role="img" aria-label="Photo of a turquoise cove beside sandstone cliffs"></div><div class="card-title">Beach Getaway to Lagos, Portugal!</div><div class="card-price">Price: 139€</div><div class="card-link">Info &amp; Book Now!</div></article>
<article class="card" style="left:836px"><div class="card-photo" role="img" aria-label="Photo of a turquoise cove beside sandstone cliffs"></div><div class="card-title">Beach Getaway to Lagos, Portugal!</div><div class="card-price">Price: 139€</div><div class="card-link">Info &amp; Book Now!</div></article>

<span class="btn btn-more">Discover more excursions!</span>

<footer class="site-footer">
  <div class="footer-col" style="left:171px;width:270px">
    <h3>About WanderlyTrips</h3>
    <p>Lorem Ipsum is simply dummy text of the printing and typesetting industry. Lorem Ipsum has been the industry's standard dummy text ever since the 1500s, when an unknown printer took a galley of type and scrambled it to make a type specimen book.</p>
  </div>
  <div class="footer-col" style="left:470px;width:250px">
    <h3>Navigate through our site!</h3>
    <ul><li>Home</li><li>About us</li><li>FAQ</li><li>Contact Us</li><li>Trip Check In</li><li>Trip Videos</li><li>Trip Departure Info</li><li>Why Travel With Us</li></ul>
  </div>
  <div class="footer-col" style="left:742px;width:287px">
    <h3>Lowest Price Guarantee!</h3>
    <p>If you find a better price elsewhere for the same trip we offer, come see us and we will beat that price!</p>
    <p style="margin-top:17px">WanderlyTrips<br>Calle Naranjo Alto 14<br>Sevilla, España 41001<br>Tel: 955 10 48 27</p>
  </div>
  <div class="social-bar">
    <span>Take a look at what trips we offer! We are also available on social netoworks!</span>
    <span class="social-icons"><span class="social-icon"></span><span class="social-icon video"></span></span>
  </div>
</footer>

</body>
</html>
```